Need corporate powerpoint template design for our sales proposals

Need corporate power point design template for our sales proposals. This powerpoint will be targeted at our customers when we are putting design proposals and pricing quotes together for them

Target Market(s)

Our customers

Industry/Entity Type

Sales

Requirements
Must have
• FernRidge name and logo somewhere
• Would like to have a cover slide and then non-cover slide as well as an ending slide for powerpoint templates
• Must have our corporate address and contact info somewhere, they are: FernRidge, Inc PO Box 47162 Oakland, California 94687. Office # 510-382-7419, email is info@fernridgeco.example
• I also attached an example business card to give you a sense of our design, also our website is www.fernridgeco.example
• Would like to match existing color scheme

```html
<!DOCTYPE html>
<html lang="en">
<head>
<meta charset="utf-8">
<title>FernRidge – Content Slide</title>
<link rel="stylesheet" href="https://fonts.googleapis.com/css2?family=Cabin:wght@700&family=Open+Sans:wght@400&family=Arimo:wght@700&display=swap">
<style>
  :root {
    --bg-light: #eaf6c8;
    --bg-mid: #d6eda4;
    --title-green: #5a7f2e;
    --body-text: #3a4a2a;
    --band-green: #77a843;
    --divider-white: #ffffff;
    --art-dark: #2b2f27;
    --art-blue: #5b97d1;
  }
  * { margin: 0; padding: 0; box-sizing: border-box; }
  html, body { width: 1200px; height: 675px; overflow: hidden; }
  body { background: #ffffff; }

  .slide {
    position: relative;
    width: 1200px;
    height: 675px;
    overflow: hidden;
    background: linear-gradient(115deg, var(--bg-light) 0%, var(--bg-mid) 55%, var(--bg-light) 100%);
  }

  .slide-title {
    position: absolute;
    left: 58px;
    top: 78px;
    font-family: "Cabin", "Gill Sans", sans-serif;
    font-weight: 700;
    font-size: 48px;
    line-height: 1.1;
    color: var(--title-green);
  }

  .slide-body {
    position: absolute;
    left: 58px;
    top: 178px;
    width: 615px;
    font-family: "Open Sans", "Segoe UI", sans-serif;
    font-weight: 400;
    font-size: 24px;
    line-height: 32.4px;
    color: var(--body-text);
  }

  .meeting-art {
    position: absolute;
    left: 698px;
    top: 216px;
    width: 394px;
    height: 173px;
    border-radius: 6px;
    background: linear-gradient(180deg, rgba(43,47,39,0.85) 0%, rgba(43,47,39,0.7) 70%, rgba(91,151,209,0.5) 100%);
  }

  .brand-mark {
    position: absolute;
    right: 28px;
    top: 490px;
    display: flex;
    align-items: center;
    gap: 8px;
    font-family: "Open Sans", "Segoe UI", sans-serif;
    font-weight: 400;
    font-size: 22px;
    color: var(--title-green);
  }
  .brand-mark .brand-dot {
    width: 14px;
    height: 14px;
    border-radius: 50%;
    background: var(--band-green);
  }

  .footer-divider {
    position: absolute;
    left: 0;
    top: 596px;
    width: 1200px;
    height: 6px;
    background: var(--divider-white);
  }

  .footer-band {
    position: absolute;
    left: 0;
    top: 603px;
    width: 1200px;
    height: 72px;
    background: var(--band-green);
    color: #ffffff;
    font-family: "Arimo", Arial, sans-serif;
    font-weight: 700;
  }

  .footer-address {
    position: absolute;
    left: 40px;
    top: 14px;
    font-size: 18px;
    line-height: 25px;
    text-align: center;
  }

  .footer-contact {
    position: absolute;
    right: 28px;
    top: 10px;
    font-size: 20px;
    line-height: 27px;
  }
</style>
</head>
<body>
  <main class="slide">
    <h1 class="slide-title">Write the title here</h1>

    <p class="slide-body">Lorem ipsum dolor sit amet,. Cras elementum bibendum tortor, id mattis lacus. Nam sed diam congue ante gravida condimentum. Aenean non nisl mattis maximus. Proin et odio mi. Suspendisse scelerisque nisi tristique, tempor sem quis, ultrices augue. Phasellus vehicula libero sed ex pharetra, vitae dapibus risus molestie. Proin rutrum veldt sit amet dapibus ullamcorper.</p>

    <div class="meeting-art" role="img" aria-label="Silhouette illustration of a business team meeting around a table with blue documents"></div>

    <div class="brand-mark">
      <span class="brand-dot"></span>
      <span class="brand-name">FernRidge</span>
    </div>

    <div class="footer-divider"></div>

    <footer class="footer-band">
      <div class="footer-address">
        FernRidge, Inc. PO Box 47162<br>
        Oakland, California 94687.
      </div>
      <div class="footer-contact">
        Office:&nbsp; 510-382-7419<br>
        Email : info@fernridgeco.example
      </div>
    </footer>
  </main>
</body>
</html>
```